Masterfolien & mehr | Branche Gesundheit | Anschlussaufträge
Tolle Leistung, netter Kontakt, verdienter Gewinner!
Zielgruppe
Sonnquell ist Dienstleister im Bereich 'Betriebliches Gesundheitsmanagement'. Zielgruppe sind Unternehmen zahlreicher Branchen, die die Gesundheit ihrer Mitarbeiter untersuchen und verbessern wollen.
Aufgabenstellung
Bitte möglichst Startfolie, Folie mit Aufzählungen und Text und Folie mit Bild und Text und Kontaktfolie.
Beispieltexte und eine entsprechende Folienansicht habe ich beigefügt, das könnte helfen.
Die Präsentation soll als E-Mail-Anhang im Nachgang eines Akquiseanrufs genutzt werden und über Produkte und Lösungen informieren.
Bitte Farbgebung berücksichtigen. Blau: 90/51/0/0, grau dunkel: 68/51/58/30, grau hell: 40/33/49/1
Schriften: Offen für Vorschläge, möglichst freie Schriften oder klassische Linotype.
Wir würden den Gewinner gern mit weiteren Aufträgen versehen, z.B. die Vorlage mit vorgegebenen Inhalten füllen, Flussdiagramme erstellen, Schaubilder erstellen etc..

```html
<!DOCTYPE html>
<html lang="de">
<head>
<meta charset="utf-8">
<title>Sonnquell – Masterfolien</title>
<link rel="stylesheet" href="https://fonts.googleapis.com/css2?family=Lato:wght@400;700&display=swap">
<style>
  :root {
    --blue: #0a6fbd;
    --blue-mid: #669fd1;
    --blue-soft: #84aad5;
    --blue-pale: #c9d8ee;
    --band: #e3eaf3;
    --grey-dark: #535b57;
    --grey-light: #a0a58e;
    --page: #e6e6e8;
    --text: #1d1d1b;
    --white: #ffffff;
  }
  * { box-sizing: border-box; margin: 0; padding: 0; }
  html, body { width: 1200px; height: 3181px; overflow: hidden; }
  body { background: var(--page); font-family: "Lato", sans-serif; color: var(--text); position: relative; }

  .slide { position: absolute; background: var(--white); overflow: hidden; }

  /* title slide */
  .slide--title { left: 78px; top: 67px; width: 1047px; height: 589px; }
  .title-photo { position: absolute; left: 0; top: 0; width: 547px; height: 589px;
    background: linear-gradient(135deg, #8a3d86 0%, #c9b9c4 38%, #e9e4de 60%, #a8c85a 100%); }
  .title-top { position: absolute; left: 547px; top: 0; width: 500px; height: 149px; background: var(--blue-soft); }
  .title-band { position: absolute; left: 428px; top: 149px; width: 619px; height: 89px; background: var(--band); opacity: .95;
    display: flex; align-items: center; padding-left: 17px; }
  .title-band h1 { font-weight: 400; font-size: 30px; color: var(--grey-dark); letter-spacing: .2px; }
  .title-panel { position: absolute; left: 547px; top: 238px; width: 500px; height: 351px; background: var(--blue);
    display: flex; align-items: center; justify-content: center; padding-top: 70px; gap: 14px; }
  .brand { font-weight: 700; font-size: 46px; color: var(--white); }
  .brand-dot { width: 22px; height: 22px; border-radius: 50%; background: var(--white); }

  /* content slides */
  .slide--content { height: 589px; }
  .slide-head { position: absolute; left: 0; top: 0; width: 100%; height: 90px; }
  .slide-head svg { position: absolute; left: 0; top: 0; }
  .slide-head h2 { position: absolute; left: 0; top: 20px; width: 690px; text-align: center;
    font-weight: 700; font-size: 29px; color: var(--white); }
  .slide-foot { position: absolute; left: 0; bottom: 0; width: 100%; height: 50px; background: var(--grey-dark);
    display: flex; align-items: center; justify-content: center; padding-left: 32px;
    font-size: 17px; color: var(--grey-light); letter-spacing: .3px; }

  .s2 { left: 77px; top: 678px; width: 1048px; }
  .s3 { left: 77px; top: 1291px; width: 1048px; }
  .s4 { left: 77px; top: 1906px; width: 1042px; }
  .s5 { left: 77px; top: 2519px; width: 1035px; height: 581px; }

  .subhead { font-weight: 700; font-size: 25px; margin-bottom: 22px; }
  .copy { font-size: 19.5px; line-height: 26px; }

  .s3 .text-col { position: absolute; left: 80px; top: 146px; width: 400px; }
  .food-photo { position: absolute; left: 542px; top: 88px; width: 506px; height: 451px;
    background: radial-gradient(ellipse at 60% 65%, #e7a24a 0%, #d9c9a6 40%, #eef0f0 75%); }

  .bullets { position: absolute; left: 88px; top: 124px; list-style: none; width: 420px; }
  .bullets li { position: relative; padding-left: 36px; font-size: 19.5px; line-height: 26px; margin-bottom: 26px; }
  .bullets li::before { content: ""; position: absolute; left: 0; top: 3px; width: 25px; height: 25px; border-radius: 50%; background: var(--blue); }
  .chart { position: absolute; left: 140px; top: 354px; }
  .s4 .text-col { position: absolute; left: 588px; top: 113px; width: 390px; }
  .s4 .copy + .copy { margin-top: 26px; }

  .s5 .text-col { position: absolute; left: 110px; top: 158px; width: 320px; text-align: center; }
  .s5 .copy { font-size: 21px; line-height: 29px; }
  .contact-brand { position: absolute; left: 110px; top: 400px; width: 320px; display: flex; justify-content: center;
    align-items: center; gap: 12px; }
  .contact-brand .brand { color: var(--grey-dark); font-size: 42px; }
  .contact-brand .brand-dot { background: var(--grey-dark); }
  .map { position: absolute; left: 538px; top: 156px; width: 356px; height: 283px; border: 2px solid var(--grey-dark);
    background: linear-gradient(120deg, #eeeeec 0%, #e4e4e2 45%, #c9e8b8 75%, #eeeeec 100%); }
</style>
</head>
<body>

<section class="slide slide--title">
  <div class="title-photo" role="img" aria-label="Foto: Gruppe beim Yoga im Kursraum"></div>
  <div class="title-top"></div>
  <div class="title-band"><h1>INVESTITION IN GESUNDHEIT - WARUM?</h1></div>
  <div class="title-panel"><span class="brand-dot"></span><span class="brand">Sonnquell</span></div>
</section>

<section class="slide slide--content s2">
  <header class="slide-head">
    <svg width="1048" height="90" viewBox="0 0 1048 90">
      <path d="M0 0H880C820 36 760 68 650 70H0Z" fill="var(--blue-mid)"/>
      <path d="M850 0H915C880 14 860 24 835 30Z" fill="var(--blue-pale)"/>
      <path d="M0 70H650C760 68 820 36 880 0H905C840 50 770 86 650 88H0Z" fill="var(--blue)"/>
    </svg>
    <h2>HEADLINE</h2>
  </header>
  <footer class="slide-foot">WWW.SONNQUELL.DE</footer>
</section>

<section class="slide slide--content s3">
  <header class="slide-head">
    <svg width="1048" height="90" viewBox="0 0 1048 90">
      <path d="M0 0H840C780 36 720 68 650 70H0Z" fill="var(--blue-mid)"/>
      <path d="M820 0H880C850 14 830 24 800 32Z" fill="var(--blue-pale)"/>
      <path d="M0 70H650C720 68 780 36 840 0H865C800 50 740 86 650 88H0Z" fill="var(--blue)"/>
    </svg>
    <h2>HEADLINE</h2>
  </header>
  <div class="text-col">
    <h3 class="subhead">Platzhaltertext</h3>
    <p class="copy">Iquat repelitia sendi verum sa que vero­rectem nietur, volecta tiuntur mi, tempe­ditis eos sit am eosaera simetur maximpo­sam venimusam, ilita si dolupta aut apite eum es aut fuga. Sed enecto omnisque aut audi optatia parum, sita enihil into es ea­tur sitaque doluptaquis aut ea ideliquis ea nam, qui reptaqui ad quam, tempori busci­tiis ute ne nonest, officium sust ratem aut venis pro bla simus que derchillab iliquas</p>
  </div>
  <div class="food-photo" role="img" aria-label="Foto: Salatschüssel, Paprika und Zwiebeln in der Küche"></div>
  <footer class="slide-foot">WWW.SONNQUELL.DE</footer>
</section>

<section class="slide slide--content s4">
  <header class="slide-head">
    <svg width="1042" height="90" viewBox="0 0 1042 90">
      <path d="M0 0H835C775 36 715 68 650 70H0Z" fill="var(--blue-mid)"/>
      <path d="M815 0H875C845 14 825 24 795 32Z" fill="var(--blue-pale)"/>
      <path d="M0 70H650C715 68 775 36 835 0H860C795 50 735 86 650 88H0Z" fill="var(--blue)"/>
    </svg>
    <h2>HEADLINE</h2>
  </header>
  <ul class="bullets">
    <li>Os sectus molupta esti aut quiscia di om­molumquam ut mo vellit</li>
    <li>Unt. Molupti cus evelitaquis con comni doluptaerum con reribusdae nesectae.</li>
    <li>Aspe molor autatium res mo dolorrovidit</li>
  </ul>
  <svg class="chart" width="325" height="140" viewBox="0 0 325 140">
    <path d="M3 110C30 80 50 60 90 62C140 66 170 78 205 74C240 70 265 60 292 54V137H3Z" fill="var(--blue)"/>
    <path d="M3 0V137H322" fill="none" stroke="var(--text)" stroke-width="3"/>
    <path d="M292 54V137" stroke="var(--text)" stroke-width="2"/>
  </svg>
  <div class="text-col">
    <h3 class="subhead">Platzhaltertext</h3>
    <p class="copy">Occus. Caborem re rerum ad ma dolupici­ae con nusandio blacepudis sim volupta­que dolo id quis consequam, cum volup­tum volores mi, ut audae. Ita di doluptias doloreiciisi as et ut re acea dolore et pro molorro dit aut lani volumenda cusciur, con ratempe rorio.</p>
    <p class="copy">Aquiberorem quidebit que consequo dis rerumenecae. Disit vendae pa dolorem. Et Evendicaerro cuptaturitae nitaten imu</p>
  </div>
  <footer class="slide-foot">WWW.SONNQUELL.DE</footer>
</section>

<section class="slide slide--content s5">
  <header class="slide-head">
    <svg width="1035" height="90" viewBox="0 0 1035 90">
      <path d="M0 0H830C770 36 710 68 650 70H0Z" fill="var(--blue-mid)"/>
      <path d="M810 0H868C840 14 820 24 790 32Z" fill="var(--blue-pale)"/>
      <path d="M0 70H650C710 68 770 36 830 0H855C790 50 730 86 650 88H0Z" fill="var(--blue)"/>
    </svg>
    <h2 style="width:680px">HEADLINE</h2>
  </header>
  <div class="text-col">
    <h3 class="subhead">Platzhaltertext</h3>
    <p class="copy">Bore eici core poreped que atemolum cum eaque nihicae­cus as aut earibus sitatat iat­que cum ipsae nis el.</p>
  </div>
  <div class="contact-brand"><span class="brand-dot"></span><span class="brand">Sonnquell</span></div>
  <div class="map" role="img" aria-label="Stadtplanausschnitt mit Standort"></div>
  <footer class="slide-foot">WWW.SONNQUELL.DE</footer>
</section>

</body>
</html>
```